Scrubbing Paper Towel Company needs Label Design

We need a product label that wraps around a roll of scrubbing paper towels as a sticker label of individually wrapped rolls. The sticker label has dimensions of 11.5" x 6" (width x height). The company logo with the brand feel and color theme is attached.

This is mainly used for dishwashing. A very large section of the label should show dishwashing and cleaning. Two very similar products can be found here :
---> https://www.shopvarnel.example/Non-Scratch-Disposable-Dish-Washing-Scrubbing-KT47M/dp/Q5283LRTVN/ref=sr_1_9?keywords=scouring+sheet&qid=2840175396&sr=8-9
--->https://www.shopvarnel.example/Zuvi-Flair-Disposable-Dish-washing-Scrubbing/dp/Q3961HWPXT/ref=sr_1_15?keywords=scouring+sheet&qid=2840175396&sr=8-15

To be included in the label:

Key points:
Did you know? Sponges are the perfect place for bacteria growth! We're talking hundreds of different species of bacteria growing in your dishwashing sponge - just as bad as the inside of your toilet. So why use a dirty sponge over and over again? Why does it smell so bad? Yes your toilet is gross, but why should the sponge go overlooked?

The Brisko Roll is a sanitary solution to this problem. Use it once, wash and reuse up to three times before throwing each sheet away - that's enough for 180 washes per roll! But don't limit yourself to dishwashing. It's great for scrubbing surfaces with hardened debris or even dry residue left from old spills. So go ahead, take a stand against bacteria and wash away knowing your kitchen is finally clean. Now that's sanitary!

Multipurpose Use:
Dishwashing
**(with example image/graphic)**
Cleaning Toilets
Cleaning Grills
Wiping Down Stoves
Cleaning Sinks
Cleaning Pet Bowls

60 Sheets
7.9" X 8.7" per sheet

Features:
Perforated for Easy Tear
Reusable
Liquid Absorbent
Non-Flammable
Cadmium Free
Kitchen Safe

```html
<!DOCTYPE html>
<html lang="en">
<head>
<meta charset="utf-8">
<title>Brisko Roll – Roll Label</title>
<link href="https://fonts.googleapis.com/css2?family=Kaushan+Script&family=Mulish:wght@400;500&family=Nunito+Sans:wght@800;900&family=Oswald:wght@400&family=Montserrat:wght@400;700&display=swap" rel="stylesheet">
<style>
  :root{
    --navy-deep:#0a1160;
    --navy:#1624a8;
    --royal:#2340d6;
    --sky:#1f8ef0;
    --accent-blue:#1f6fd0;
    --white:#ffffff;
    --silver-light:#f4f4f6;
    --silver:#c9cad0;
    --silver-dark:#9a9ba3;
    --text-navy:#1a2380;
  }
  *{margin:0;padding:0;box-sizing:border-box}
  html,body{width:1200px;height:683px;overflow:hidden;background:var(--navy-deep)}
  .label{position:relative;width:1200px;height:683px;overflow:hidden;
    background:radial-gradient(ellipse at 52% 40%, var(--royal) 0%, var(--navy) 45%, var(--navy-deep) 100%);
    font-family:"Mulish",sans-serif;color:var(--white)}
  .backdrop{position:absolute;inset:0;width:1200px;height:683px}
  .script-heading{font-family:"Kaushan Script",cursive;font-size:24px;font-weight:400;position:absolute}
  .key-points .script-heading{left:0;top:0}
  .key-points{position:absolute;left:48px;top:44px;width:298px}
  .key-points p{font-size:12.6px;line-height:21px;text-align:justify;hyphens:auto;position:absolute;left:0;width:298px}
  .key-points .intro{top:44px}
  .key-points .solution{top:233px}
  .features{position:absolute;left:897px;top:72px}
  .features .script-heading{left:2px;top:0}
  .feature-list{list-style:none;position:absolute;top:44px;left:0;width:290px}
  .feature-list li{font-family:"Nunito Sans",sans-serif;font-weight:800;font-size:19px;line-height:32.3px;white-space:nowrap;display:flex;align-items:center}
  .feature-list li::before{content:"";width:9px;height:9px;border-radius:50%;background:var(--sky);margin-right:8px;flex:none}
  .brand{position:absolute;left:380px;top:150px;width:440px;text-align:center}
  .brand-name{font-family:"Nunito Sans",sans-serif;font-weight:900;font-size:78px;line-height:1;color:var(--white);letter-spacing:-1px}
  .tagline{font-family:"Nunito Sans",sans-serif;font-weight:800;font-size:24px;color:var(--white);margin-top:14px}
  .use-badge{position:absolute;width:140px;height:140px;margin:-70px 0 0 -70px;border-radius:50%;
    background:linear-gradient(160deg,var(--silver-light),var(--silver) 55%,var(--silver-dark));
    box-shadow:0 4px 10px rgba(0,0,30,.35);display:flex;align-items:center;justify-content:center}
  .use-badge .disc{width:122px;height:122px;border-radius:50%;
    background:radial-gradient(circle at 50% 35%, var(--royal) 0%, var(--navy) 55%, var(--navy-deep) 100%);
    display:flex;flex-direction:column;align-items:center;justify-content:center;gap:6px}
  .use-badge .icon-area{width:50px;height:44px;border-radius:10px;background:rgba(150,170,255,.28)}
  .use-badge .use-name{font-family:"Oswald",sans-serif;font-size:16.5px;line-height:19px;text-align:center;color:var(--white)}
  .pack-size{position:absolute;right:52px;top:548px;text-align:right}
  .sheet-count{font-family:"Montserrat",sans-serif;font-weight:700;font-size:44px;line-height:1;color:var(--accent-blue)}
  .sheet-size{font-family:"Montserrat",sans-serif;font-weight:400;font-size:30px;line-height:1;color:var(--text-navy);margin-top:8px}
</style>
</head>
<body>
<main class="label">
  <svg class="backdrop" viewBox="0 0 1200 683" aria-hidden="true">
    <defs>
      <linearGradient id="floor-fill" x1="0" y1="0" x2="0" y2="1">
        <stop offset="0" stop-color="#f2f2f4"/>
        <stop offset="0.5" stop-color="#d9d9dd"/>
        <stop offset="1" stop-color="#b4b5bb"/>
      </linearGradient>
    </defs>
    <path d="M0,552 C200,612 420,588 640,505 S1040,400 1200,462 L1200,683 L0,683 Z" fill="url(#floor-fill)"/>
    <path d="M0,552 C200,612 420,588 640,505 S1040,400 1200,462" fill="none" stroke="#ffffff" stroke-width="4"/>
  </svg>

  <section class="key-points">
    <h2 class="script-heading">Key points:</h2>
    <p class="intro">Did you know? Sponges are the perfect place for bacteria growth! We're talking hundreds of different species of bacteria growing in your dishwashing sponge - just as bad as the inside of your toilet. So why use a dirty sponge over and over again? Why does it smell so bad? Yes your toilet is gross, but why should the sponge go overlooked?</p>
    <p class="solution">The Brisko Roll is a sanitary solution to this problem. Use it once, wash and reuse up to three times before throwing each sheet away - that's enough for 180 washes per roll! But don't limit yourself to dishwashing. It's great for scrubbing surfaces with hardened debris or even dry residue left from old spills. So go ahead, take a stand against bacteria and wash away knowing your kitchen is finally clean. Now that's sanitary!</p>
  </section>

  <div class="brand">
    <h1 class="brand-name">Brisko Roll</h1>
    <p class="tagline">Clean Smarter, Not Harder</p>
  </div>

  <section class="features">
    <h2 class="script-heading">Features:</h2>
    <ul class="feature-list">
      <li>Perforated for Easy Tear</li>
      <li>Reusable</li>
      <li>Liquid Absorbent</li>
      <li>Non-Flammable</li>
      <li>Cadmium Free</li>
      <li>Kitchen Safe</li>
    </ul>
  </section>

  <div class="use-badge" style="left:170px;top:558px"><div class="disc"><div class="icon-area" role="img" aria-label="Dishwashing icon: hand scrubbing a plate"></div><span class="use-name">Dishwashing</span></div></div>
  <div class="use-badge" style="left:362px;top:533px"><div class="disc"><div class="icon-area" role="img" aria-label="Toilet icon with sparkles"></div><span class="use-name">Cleaning Toilets</span></div></div>
  <div class="use-badge" style="left:537px;top:489px"><div class="disc"><div class="icon-area" role="img" aria-label="Grill icon"></div><span class="use-name">Cleaning Grills</span></div></div>
  <div class="use-badge" style="left:708px;top:451px"><div class="disc"><div class="icon-area" role="img" aria-label="Stove top icon"></div><span class="use-name">Wiping Down<br>Stoves</span></div></div>
  <div class="use-badge" style="left:884px;top:410px"><div class="disc"><div class="icon-area" role="img" aria-label="Sink with faucet icon"></div><span class="use-name">Cleaning Sinks</span></div></div>
  <div class="use-badge" style="left:1051px;top:439px"><div class="disc"><div class="icon-area" role="img" aria-label="Pet food bowl icon"></div><span class="use-name">Cleaning Pet<br>Bowls</span></div></div>

  <div class="pack-size">
    <p class="sheet-count">60 SHEETS</p>
    <p class="sheet-size">7.9" X 8.7" PER SHEET</p>
  </div>
</main>
</body>
</html>
```